Brightpath Letterhead

We would like a letterhead for our company. I have uploaded our logo.

Brightpath Ridge Consulting
1450 W Corliss Ave Ste 310
Cedar Hollow, TX 75482
833-517-2906

```html
<!DOCTYPE html>
<html lang="en">
<head>
<meta charset="utf-8">
<title>Brightpath Letterhead</title>
<link rel="stylesheet" href="https://fonts.googleapis.com/css2?family=Open+Sans:wght@400;600&family=Source+Sans+3:wght@400&display=swap">
<style>
  :root {
    --backdrop: #e4e4e4;
    --paper: #ffffff;
    --brand-dark: #0e4a5a;
    --brand-green: #5cbf8f;
    --rule: #4aa591;
    --text: #474747;
    --footer-text: #3c3c3c;
  }
  html, body {
    margin: 0;
    padding: 0;
    width: 1200px;
    height: 1141px;
    overflow: hidden;
    background: var(--backdrop);
  }
  .letterhead {
    position: absolute;
    left: 207px;
    top: 20px;
    width: 785px;
    height: 1100px;
    background: var(--paper);
    box-shadow: 0 3px 10px rgba(0,0,0,0.18);
    font-family: "Source Sans 3", sans-serif;
    color: var(--text);
  }
  .brand {
    position: absolute;
    top: 59px;
    left: 0;
    right: 0;
    display: flex;
    justify-content: center;
    align-items: center;
    gap: 10px;
  }
  .brand-dot {
    width: 40px;
    height: 40px;
    border-radius: 50%;
    background: var(--brand-green);
  }
  .brand-name {
    font-family: "Open Sans", sans-serif;
    font-weight: 600;
    font-size: 19px;
    line-height: 21px;
    letter-spacing: 0.08em;
    color: var(--brand-dark);
    text-transform: uppercase;
  }
  .brand-name span { display: block; }
  .recipient {
    position: absolute;
    left: 59px;
    top: 284px;
  }
  .recipient p { margin: 0; }
  .recipient-name {
    font-size: 15.5px;
    line-height: 20px;
    text-transform: uppercase;
    margin-bottom: 1px !important;
  }
  .recipient-line {
    font-size: 11.6px;
    line-height: 19px;
  }
  .body-copy {
    position: absolute;
    left: 59px;
    top: 379px;
    width: 667px;
  }
  .body-copy p {
    margin: 0 0 16px;
    font-size: 11.9px;
    line-height: 19.3px;
    text-align: justify;
  }
  .closing {
    position: absolute;
    left: 59px;
    top: 684px;
    font-size: 12.6px;
    margin: 0;
  }
  .signature {
    position: absolute;
    left: 59px;
    top: 712px;
    width: 158px;
    height: 34px;
    background: linear-gradient(90deg, rgba(14,74,90,0.16), rgba(14,74,90,0.08));
    border-radius: 4px;
  }
  .footer {
    position: absolute;
    left: 159px;
    width: 466px;
    top: 1030px;
    font-family: "Open Sans", sans-serif;
  }
  .footer-phone {
    display: flex;
    align-items: center;
    gap: 6px;
    font-size: 12.3px;
    color: var(--footer-text);
    height: 20px;
  }
  .footer-rule {
    flex: 1;
    height: 1px;
    background: var(--rule);
  }
  .footer-phone svg { width: 12px; height: 12px; }
  .footer-address {
    margin: 2px 0 0;
    font-size: 13px;
    color: var(--footer-text);
    text-align: center;
    white-space: nowrap;
  }
  .footer-company {
    color: var(--brand-dark);
    font-weight: 600;
  }
</style>
</head>
<body>
  <main class="letterhead">
    <header class="brand">
      <span class="brand-dot"></span>
      <span class="brand-name"><span>Brightpath Ridge</span><span>Consulting</span></span>
    </header>

    <section class="recipient">
      <p class="recipient-name">Darren Holloway</p>
      <p class="recipient-line">President / CEO</p>
      <p class="recipient-line">City/State, Zip Code</p>
    </section>

    <section class="body-copy">
      <p>Lorem Ipsum is simply dummy text of the printing and typesetting industry. Lorem Ipsum has been the industry's standard dummy text ever since the 1500s, when an unknown printer took a galley of type and scrambled it to make a type specimen book. It has survived not only five centuries, but also the leap into electronic typesetting, remaining essentially unchanged. It was popularised in the 1960s with the release of Marlowset sheets containing Lorem Ipsum passages, and more recently with desktop publishing software like Quillbook Layout including versions of Lorem Ipsum.</p>
      <p>It is a long established fact that a reader will be distracted by the readable content of a page when looking at its layout. The point of using Lorem Ipsum is that it has a more-or-less normal distribution of letters, as opposed to using 'Content here, content here', making it look like readable English. Many desktop publishing packages and web page editors now use Lorem Ipsum as their default model text, and a searchaccident, sometimes on purpose (injected humour and the like).</p>
      <p>There are many variations of passages of Lorem Ipsum available, but the majority have suffered alteration in some form, by injected humour, or randomised words which don't look even slightly believable. If you are going to use a passage of Lorem Ipsum, you need to be sure there isn't anything embarrassing hidden in the middle of text.</p>
    </section>

    <p class="closing">Sincerely,</p>
    <div class="signature" role="img" aria-label="Handwritten signature"></div>

    <footer class="footer">
      <div class="footer-phone">
        <span class="footer-rule"></span>
        <svg viewBox="0 0 24 24" aria-hidden="true">
          <path fill="var(--brand-green)" d="M6.6 10.8a15.1 15.1 0 0 0 6.6 6.6l2.2-2.2a1 1 0 0 1 1-.25 11.4 11.4 0 0 0 3.6.57 1 1 0 0 1 1 1V20a1 1 0 0 1-1 1A17 17 0 0 1 3 4a1 1 0 0 1 1-1h3.5a1 1 0 0 1 1 1c0 1.25.2 2.45.57 3.57a1 1 0 0 1-.25 1z"/>
        </svg>
        <span>833-517-2906</span>
        <span class="footer-rule"></span>
      </div>
      <p class="footer-address"><span class="footer-company">Brightpath Ridge Consulting -</span> 1450 W Corliss Ave Ste 310, Cedar Hollow, TX 75482</p>
    </footer>
  </main>
</body>
</html>
```